Security Business card

I need a new business card for my new company Bastion Crest Security Group we provide security for clubs,pubs,hotels etc. I would like to see the main colors red and black to be used. The final design should communicate honor and integrity.

Industry/Entity Type

Security

Contact Information for Business Card

Marcus Delvane
Company Name-Bastion Crest Security Group
Abn-47318265094
Acn-318265094
address- po box 7352 Ferndale nsw 2291
phone- 0437682915
email- Marcus@bastioncrest.com.au

```html
<!DOCTYPE html>
<html lang="en">
<head>
<meta charset="utf-8">
<title>Bastion Crest Security Group – Business Card</title>
<link rel="stylesheet" href="https://fonts.googleapis.com/css2?family=Source+Sans+3:wght@400;600&display=swap">
<style>
  :root {
    --backdrop: #1b1b1b;
    --card-white: #ffffff;
    --brand-red: #e31e2d;
    --ink: #1a1a1a;
    --on-red: #ffffff;
  }
  * { box-sizing: border-box; margin: 0; padding: 0; }
  html, body {
    width: 1200px;
    height: 1021px;
    overflow: hidden;
    background: var(--backdrop);
    font-family: "Source Sans 3", "Myriad Pro", Arial, sans-serif;
  }
  .business-card {
    position: absolute;
    left: 150px;
    top: 235px;
    width: 900px;
    height: 550px;
    display: flex;
    box-shadow: 0 20px 50px rgba(0,0,0,.5);
  }
  .card-brand {
    width: 400px;
    background: var(--card-white);
    display: flex;
    flex-direction: column;
    align-items: center;
    justify-content: center;
    padding: 0 36px;
    text-align: center;
  }
  .brand-mark {
    width: 120px;
    height: 120px;
    border-radius: 50%;
    background: var(--brand-red);
    margin-bottom: 34px;
  }
  .brand-name {
    font-size: 30px;
    font-weight: 400;
    color: var(--ink);
    letter-spacing: -0.5px;
    line-height: 1.1;
  }
  .brand-tagline {
    margin-top: 14px;
    font-size: 22px;
    color: var(--ink);
    line-height: 1.15;
  }
  .card-contact {
    flex: 1;
    background: var(--brand-red);
    color: var(--on-red);
    padding: 70px 40px 0 48px;
    position: relative;
  }
  .holder-name {
    font-size: 52px;
    font-weight: 400;
    letter-spacing: -0.5px;
    line-height: 1;
  }
  .company-ids {
    margin-top: 10px;
    font-size: 18px;
    line-height: 1.15;
  }
  .contact-list {
    position: absolute;
    left: 28px;
    bottom: 150px;
    list-style: none;
  }
  .contact-item {
    display: flex;
    align-items: center;
    gap: 10px;
    font-size: 25px;
    line-height: 1.3;
  }
  .contact-icon {
    width: 22px;
    height: 22px;
    flex: none;
    fill: var(--on-red);
  }
</style>
</head>
<body>
  <article class="business-card">
    <section class="card-brand">
      <div class="brand-mark" aria-hidden="true"></div>
      <h1 class="brand-name">Bastion Crest Security Group</h1>
      <p class="brand-tagline">We specialize in providing security<br>for clubs, pubs and hotels</p>
    </section>
    <section class="card-contact">
      <h2 class="holder-name">Marcus Delvane</h2>
      <p class="company-ids">ABN-47318265094<br>ACN-318265094</p>
      <ul class="contact-list">
        <li class="contact-item">
          <svg class="contact-icon" viewBox="0 0 24 24" aria-hidden="true"><path d="M12 3 1 12h3v9h6v-6h4v6h6v-9h3z"/></svg>
          po box 7352 Ferndale nsw 2291
        </li>
        <li class="contact-item">
          <svg class="contact-icon" viewBox="0 0 24 24" aria-hidden="true"><path d="M2 5h20v14H2z M3.5 6.5 12 13l8.5-6.5" stroke="#e31e2d" stroke-width="1.5"/></svg>
          Marcus@bastioncrest.com.au
        </li>
        <li class="contact-item">
          <svg class="contact-icon" viewBox="0 0 24 24" aria-hidden="true"><path d="M6.6 10.8a15 15 0 0 0 6.6 6.6l2.2-2.2c.3-.3.7-.4 1-.2 1.1.4 2.3.6 3.6.6.6 0 1 .4 1 1V20c0 .6-.4 1-1 1A17 17 0 0 1 3 4c0-.6.4-1 1-1h3.5c.6 0 1 .4 1 1 0 1.3.2 2.5.6 3.6.1.3 0 .7-.2 1z"/></svg>
          0437682915
        </li>
      </ul>
    </section>
  </article>
</body>
</html>
```